Business Card Design Project

Corvexa logo will be provided after
Front

Ned Marrowick- Construction Manager

Ph: (61) 07 53182079
nmarrowick@corvexa-example.com.au
PO Box 83 Kelvorin 4619

Back
Corvexa
EPCM

Oil - Gas - Mining

Industry/Entity Type

Business

Font styles to use
Sans Serif

Colors
faa54b

Requirements
Must have
• White Back Ground

```html
<!DOCTYPE html>
<html lang="en">
<head>
<meta charset="utf-8">
<title>Corvexa Business Cards</title>
<link rel="stylesheet" href="https://fonts.googleapis.com/css2?family=Exo+2:wght@600;800&family=Open+Sans:wght@500&family=Crimson+Pro:wght@400&family=Noto+Sans+Mono:wght@400&display=swap">
<style>
  :root {
    --orange: #faa54b;
    --orange-deep: #f28c1f;
    --ink: #1c1c1c;
    --ink-soft: #333333;
    --card: #ffffff;
    --backdrop: #e4e4e4;
  }
  * { box-sizing: border-box; margin: 0; padding: 0; }
  html, body { width: 1200px; height: 900px; overflow: hidden; }
  body {
    background: var(--backdrop);
    display: flex;
    align-items: center;
    justify-content: center;
    gap: 40px;
  }
  .card {
    position: relative;
    width: 520px;
    height: 300px;
    background: var(--card);
    overflow: hidden;
    box-shadow: 0 6px 18px rgba(0,0,0,.18);
  }

  /* Back side */
  .card-back .brand {
    position: absolute;
    left: 44px;
    top: 70px;
    display: flex;
    align-items: center;
    gap: 12px;
  }
  .brand-name {
    font-family: "Exo 2", sans-serif;
    font-weight: 800;
    color: var(--ink);
    letter-spacing: 2px;
    line-height: 1;
    white-space: nowrap;
  }
  .card-back .brand-name { font-size: 54px; }
  .brand-dot {
    width: 18px; height: 18px;
    border-radius: 50%;
    background: var(--orange);
    flex: none;
  }
  .card-back .division {
    position: absolute;
    left: 90px;
    top: 142px;
    font-family: "Exo 2", sans-serif;
    font-weight: 600;
    font-size: 22px;
    letter-spacing: 22px;
    color: var(--orange-deep);
  }
  .card-back .skyline {
    position: absolute;
    right: 0;
    bottom: 0;
    width: 340px;
    height: 190px;
    background: linear-gradient(165deg, rgba(28,28,28,0) 30%, rgba(28,28,28,.55) 65%, var(--ink) 100%);
    clip-path: polygon(100% 0, 100% 100%, 0 100%, 0 70%);
  }

  /* Front side */
  .card-front .person {
    position: absolute;
    left: 28px;
    top: 34px;
  }
  .person-name {
    font-family: "Open Sans", sans-serif;
    font-weight: 500;
    font-size: 22px;
    color: var(--ink);
  }
  .person-role {
    font-family: "Crimson Pro", serif;
    font-size: 18px;
    color: var(--ink-soft);
    margin-top: 4px;
  }
  .card-front .brand {
    position: absolute;
    right: 26px;
    top: 26px;
    display: flex;
    align-items: center;
    gap: 7px;
  }
  .card-front .brand-name { font-size: 24px; letter-spacing: 1px; }
  .card-front .brand-dot { width: 9px; height: 9px; }

  .contact {
    position: absolute;
    left: 196px;
    top: 100px;
    display: flex;
    gap: 9px;
  }
  .contact-icons {
    display: flex;
    flex-direction: column;
    gap: 6px;
    padding-top: 3px;
  }
  .contact-icons svg { width: 18px; height: 18px; display: block; }
  .contact-rule { width: 2px; background: var(--orange-deep); }
  .contact-lines {
    list-style: none;
    font-family: "Noto Sans Mono", monospace;
    font-size: 13px;
    line-height: 24px;
    color: var(--ink);
    white-space: nowrap;
  }

  .band-line {
    position: absolute;
    left: 0; right: 0;
    top: 184px;
    height: 2px;
    background: var(--orange-deep);
  }
  .band {
    position: absolute;
    left: 0; right: 0;
    top: 190px;
    bottom: 10px;
    background: var(--orange);
  }
  .band .skyline {
    position: absolute;
    inset: 0;
    background: linear-gradient(180deg, rgba(28,28,28,0) 10%, rgba(28,28,28,.35) 55%, rgba(28,28,28,.8) 100%);
  }
  .band-base {
    position: absolute;
    left: 0; right: 0;
    bottom: 4px;
    height: 3px;
    background: var(--ink);
  }
</style>
</head>
<body>
  <section class="card card-back" aria-label="Card back">
    <div class="brand">
      <span class="brand-name">CORVEXA</span>
      <span class="brand-dot"></span>
    </div>
    <div class="division">EPCM</div>
    <div class="skyline" role="img" aria-label="Silhouette of a pump jack and drilling derricks"></div>
  </section>

  <section class="card card-front" aria-label="Card front">
    <div class="person">
      <p class="person-name">Ned Marrowick</p>
      <p class="person-role">Construction Manager</p>
    </div>
    <div class="brand">
      <span class="brand-name">CORVEXA</span>
      <span class="brand-dot"></span>
    </div>

    <div class="contact">
      <div class="contact-icons">
        <svg viewBox="0 0 20 20" aria-label="Phone"><circle cx="10" cy="10" r="8.6" fill="none" stroke="#1c1c1c" stroke-width="1.4"/><path d="M6.6 5.8c.6-.5 1.2-.4 1.5.1l.8 1.4c.2.5 0 .9-.4 1.2l-.5.3c.4 1 1.3 2 2.4 2.6l.4-.5c.3-.4.8-.5 1.2-.3l1.4.8c.5.3.6.9.1 1.5-.8.9-2 1-3.2.3-1.7-1-3-2.5-3.9-4.2-.6-1.2-.6-2.4.2-3.2z" fill="#1c1c1c"/></svg>
        <svg viewBox="0 0 20 20" aria-label="Mail"><circle cx="10" cy="10" r="8.6" fill="none" stroke="#1c1c1c" stroke-width="1.4"/><rect x="5.2" y="6.8" width="9.6" height="6.6" fill="#1c1c1c"/><path d="M5.4 7l4.6 3.6L14.6 7" fill="none" stroke="#fff" stroke-width="1"/></svg>
        <svg viewBox="0 0 20 20" aria-label="Email"><circle cx="10" cy="10" r="8.6" fill="none" stroke="#1c1c1c" stroke-width="1.4"/><text x="10" y="13.6" text-anchor="middle" font-family="Open Sans, sans-serif" font-size="10" font-weight="700" fill="#1c1c1c">@</text></svg>
      </div>
      <div class="contact-rule"></div>
      <ul class="contact-lines">
        <li>(61) 07 53182079</li>
        <li>PO Box 83 Kelvorin 4619</li>
        <li>nmarrowick@corvexa-example.com.au</li>
      </ul>
    </div>

    <div class="band-line"></div>
    <div class="band">
      <div class="skyline" role="img" aria-label="Silhouette of a pump jack and drilling derricks"></div>
    </div>
    <div class="band-base"></div>
  </section>
</body>
</html>
```